Professional Website Design to match new logo for Medical Legal Company

We have rebranded our company and We want a professional but also dynamic web site design for a group of esteemed doctors that provide expert evaluation of an injured worker in a Workers Compensation case.
​
1. Our target market is both the attorneys who select our doctors and any doctors who would wish to join our group.

2. Notes for the Landing Page:
- We prefer a simpler, sleeker more modern look for the landing page.
- We want a simplified landing page with one image, three buttons highlighted in Content document.
- We want the main image to be black and white but it can be splashed with color.
-We think the landing page might be enhanced by add a dark blue or black as a primary color. Of course please feel free to try any color combination you think might work.
- We want "The Meridale Circle" in large letters and "Stewards of a fair and prompt outcome" in small lettering. We don't want icons on the buttons.
- Do not want more than the one picture at top of landing page.
- We do not want any pictures that include faces. Please eliminate or replace. They will not be chosen.
- For the landing page, instead of a second set of photos please experiment with using medical symbols and legal symbols.
​
3. New Company Name: The Meridale Circle
New logo is uploaded bronze and grey/silver will be colors although we are still tweaking the colors for more metallic feel. Want simple not busy.

4. The overall Web page design needs to have some website design effect (e,g image rollover, scrolling effect, hover effect etc).

5. Please follow the attached word document file for the page content of the 4 web pages. Do not mix it up.

Previous company website: www.clinicjuristpanel.example (we wish to convert some of the content from this website to the new brand). Competitor website that we like: www.docboardly.example

Target Market(s)

Professional Elite. Attorneys and Doctors

Industry/Entity Type

Medical Legal

Coding

Coded - Design and coding required

Number of Pages Required

5+ page

Font styles to use
Other font styles liked:
• Helvetica or maybe font that matches logo. We are open

Colors

Designer to choose colors to be used in the design.

Requirements
Must have
• I can't locate on color scale but we want Bronze and Silver/Grey from logo. Additional colors can be added. Various shades of grey
Nice to have
• Black and white photos, simple elegant design
Should not have
• Images with faces of unknown people

```html
<!DOCTYPE html>
<html lang="en">
<head>
<meta charset="utf-8">
<title>The Meridale Circle</title>
<link href="https://fonts.googleapis.com/css2?family=Archivo:wght@700;800&family=Roboto:wght@400;500;700&display=swap" rel="stylesheet">
<style>
:root{
  --navy:#02041f;
  --navy-mid:#0c1a44;
  --footer:#05061a;
  --bronze:#c7814f;
  --bronze-dark:#8a5428;
  --grey-title:#77767d;
  --grey-btn-top:#7a7a80;
  --grey-btn-bottom:#3f3f45;
  --frame:#2c3352;
  --white:#ffffff;
  --text-dark:#555;
}
*{box-sizing:border-box;margin:0;padding:0}
html,body{width:953px;height:1200px;overflow:hidden}
body{
  position:relative;
  font-family:"Roboto",Arial,sans-serif;
  color:var(--white);
  background:var(--navy);
}
.city-backdrop{
  position:absolute;left:0;top:330px;width:953px;height:766px;
  background:
    radial-gradient(ellipse 60px 420px at 45px 560px, rgba(40,110,220,.45), transparent 70%),
    linear-gradient(180deg, var(--navy) 0%, var(--navy-mid) 45%, #1b2450 75%, #2a2638 100%);
}
.site-header{position:absolute;left:114px;top:22px;width:725px;height:46px;display:flex;align-items:center;justify-content:space-between}
.brand{display:flex;align-items:center;gap:9px;font-weight:500;font-size:20px;color:#9a9aa2}
.brand-mark{width:14px;height:14px;background:var(--bronze)}
.main-nav{display:flex;gap:17px;font-size:11.5px;font-weight:500}
.main-nav a{color:var(--white);text-decoration:none}
.main-nav a+a{margin-left:3px}
.hero-title{position:absolute;top:118px;width:953px;text-align:center;font-family:"Archivo",Helvetica,sans-serif;font-weight:800;font-size:41px;letter-spacing:.5px;color:var(--grey-title)}
.hero-title span{color:var(--bronze)}
.tagline{position:absolute;top:178px;width:953px;text-align:center;font-size:14.5px;font-weight:500}
.hero-frame{position:absolute;left:111px;top:232px;width:731px;height:413px;border-radius:16px;background:var(--frame);padding:9px}
.hero-photo{width:100%;height:100%;border-radius:11px;background:linear-gradient(120deg,#b8956a 0%,#d9c7a8 35%,#e9e6df 55%,#6e5438 80%,#2a2420 100%)}
.intro{position:absolute;left:130px;top:686px;width:693px;text-align:center;font-size:16px;font-weight:500;line-height:30.5px}
.choices{position:absolute;left:194px;top:810px;display:flex;gap:17px}
.choice{width:177px;height:63px;border-radius:7px;display:flex;flex-direction:column;align-items:center;justify-content:center;font-size:11.5px;font-weight:500;text-transform:uppercase;background:linear-gradient(180deg,var(--grey-btn-top),var(--grey-btn-bottom))}
.choice.primary{background:linear-gradient(180deg,#d28e5e,var(--bronze-dark))}
.choice small{font-size:8.5px;text-transform:none;font-weight:400;margin-top:6px}
.newsletter-title{position:absolute;top:934px;width:953px;text-align:center;font-family:"Archivo",Helvetica,sans-serif;font-weight:700;font-size:22px}
.signup{position:absolute;left:170px;top:990px;width:613px;height:61px;border-radius:9px;background:#4d4f5c;padding:7px}
.signup-inner{display:flex;align-items:center;justify-content:space-between;height:100%;background:var(--white);border-radius:7px;padding:3px 4px 3px 13px}
.signup-inner span{color:var(--text-dark);font-size:11px}
.signup-btn{width:206px;height:41px;border-radius:3px;background:linear-gradient(180deg,#c27a45,#8e5629);display:flex;align-items:center;justify-content:center;font-weight:700;font-size:12.5px}
.site-footer{position:absolute;left:0;top:1096px;width:953px;height:104px;background:var(--footer)}
.site-footer .brand{position:absolute;left:114px;top:32px;font-size:17px}
.contact{position:absolute;display:flex;gap:7px;font-size:10px;line-height:14px}
.contact b{font-weight:700;font-size:8.5px;display:block}
.contact svg{flex:none;margin-top:1px}
.copyright{position:absolute;left:330px;top:76px;font-size:8.5px}
</style>
</head>
<body>
<div class="city-backdrop" role="img" aria-label="Night city skyline with a lit tower along the left edge"></div>

<header class="site-header">
  <div class="brand"><span class="brand-mark"></span>The Meridale Circle</div>
  <nav class="main-nav"><a href="#">Physicians</a><a href="#">Stakeholder</a><a href="#">Meridale Gives</a></nav>
</header>

<h1 class="hero-title">THE MERIDALE <span>CIRCLE</span></h1>
<p class="tagline">Stewards of a fair and prompt outcome</p>

<div class="hero-frame">
  <div class="hero-photo" role="img" aria-label="Two professionals at a desk with charts, a gavel and scales of justice, faces not shown"></div>
</div>

<p class="intro">The Meridale Circle is a leader in Qualified Medical Evaluations and SIBTF cases in the State of California. Our doctors are dedicated to facilitating settlements through rapid, objective and well researched Expert Medical Opinions</p>

<div class="choices">
  <a class="choice primary">Stakeholders<small>Attorneys, Carriers, Injured worker</small></a>
  <a class="choice">Our Physicians</a>
  <a class="choice">Member Physicians</a>
</div>

<h2 class="newsletter-title">MOST RECENT NEWSLETTER</h2>
<form class="signup">
  <div class="signup-inner"><span>Enter Email Address</span><div class="signup-btn">DOWNLOAD NOW</div></div>
</form>

<footer class="site-footer">
  <div class="brand"><span class="brand-mark"></span>The Meridale Circle</div>
  <div class="contact" style="left:331px;top:24px">
    <svg width="10" height="10" viewBox="0 0 24 24"><path fill="#c7814f" d="M6.6 10.8a15 15 0 0 0 6.6 6.6l2.2-2.2a1 1 0 0 1 1-.25 11.4 11.4 0 0 0 3.6.57 1 1 0 0 1 1 1V20a1 1 0 0 1-1 1A17 17 0 0 1 3 4a1 1 0 0 1 1-1h3.5a1 1 0 0 1 1 1c0 1.25.2 2.45.57 3.57a1 1 0 0 1-.25 1z"/></svg>
    <div><b>Call toll free</b>(800) 555-0142</div>
  </div>
  <div class="contact" style="left:454px;top:24px">
    <svg width="12" height="10" viewBox="0 0 24 20"><rect x="1" y="2" width="22" height="16" rx="2" fill="#c7814f"/><path d="M2 4l10 7 10-7" stroke="#05061a" stroke-width="2" fill="none"/></svg>
    <div><b>Fax</b>(310) 555-0187</div>
  </div>
  <div class="contact" style="left:578px;top:17px">
    <svg width="8" height="11" viewBox="0 0 16 22"><path fill="#c7814f" d="M8 0a8 8 0 0 0-8 8c0 6 8 14 8 14s8-8 8-14a8 8 0 0 0-8-8zm0 11a3 3 0 1 1 0-6 3 3 0 0 1 0 6z"/></svg>
    <div><b>Location</b>2250 Larkspur Ave. 4th Floor Fernhollow, CA 90415</div>
  </div>
  <p class="copyright">Copyright © 2024 Meridale Circle. All rights reserved.</p>
</footer>
</body>
</html>
```